Business cards for start-up accounting firm

I'm looking for a double sided business card ready for upload into Lumo print or similar print providers with no modification required by me.
I'm looking for something simple as i think cards that are too 'busy' actually detract from the message. I have some thoughts but more than happy to see what comes up. The logo i have came out of left field and i love it the moment i saw it!

My thoughts:

Side 1: Just the logo, perhaps on a dark grey or charcoal background to make the logo colours stand out?

Side 2: The call to action from me website 'Looking for a more relaxed, friendly and interactive relationship with your accountant?' with my contact information
Name: Gus Tarrow
Email: gus@ledgerowl.com.au
Website: www.ledgerowl.com.au
Phone: 1300 762 349

The call to action needs to be the first thing they see when they look at side 2. If it helps to know what we do and how we do it there is a draft website at www.ledgerowl.com.au

Like i said, happy to consider anything that comes up :)

Target Market(s)

i'm targeting small business owners who experience a lot of stress around finacial reporting and have had bad experiences with accountants in the past.

Industry/Entity Type

Accounting

Contact Information for Business Card

Contained in the Description

Font styles to use
Serif
Sans Serif
Other font styles liked:
• See logo files attached

Colors
474747

Requirements
Must have
• My logo, slogan and contact information

```html
<!DOCTYPE html>
<html lang="en">
<head>
<meta charset="utf-8">
<title>Ledger Owl – Business Card</title>
<link rel="stylesheet" href="https://fonts.googleapis.com/css2?family=Exo+2:wght@600;700&family=PT+Sans+Narrow&display=swap">
<style>
  :root {
    --backdrop: #ece9e4;
    --charcoal: #474747;
    --charcoal-light: #8d8d8d;
    --paper: #ffffff;
    --ink: #1d1d1d;
    --plum: #8a3577;
    --sun: #f4c600;
    --band-start: #e6e6ea;
  }
  * { margin: 0; padding: 0; box-sizing: border-box; }
  html, body { width: 1200px; height: 375px; overflow: hidden; }
  body {
    position: relative;
    background: var(--backdrop);
    font-family: "Exo 2", sans-serif;
  }
  .card {
    position: absolute;
    width: 525px;
    height: 300px;
    box-shadow: 0 1px 4px rgba(0,0,0,0.18);
  }
  /* Front */
  .card--front {
    left: 50px; top: 36px;
    background: radial-gradient(ellipse 60% 70% at 50% 48%, var(--charcoal-light) 0%, var(--charcoal) 78%);
    display: flex;
    align-items: center;
    justify-content: center;
  }
  .brand {
    font-family: "Exo 2", sans-serif;
    font-weight: 700;
    font-size: 52px;
    letter-spacing: 1px;
    color: var(--sun);
    line-height: 1;
  }
  /* Back */
  .card--back {
    left: 622px; top: 35px;
    background: var(--paper);
  }
  .call-to-action {
    position: absolute;
    left: 73px; top: 30px;
    font-family: "Exo 2", sans-serif;
    font-weight: 600;
    font-size: 16.5px;
    line-height: 19px;
    color: var(--ink);
  }
  .band {
    position: absolute;
    left: 0; right: 0;
    height: 11px;
  }
  .band--plum { top: 80px; background: linear-gradient(90deg, var(--band-start), var(--plum)); }
  .band--sun { top: 264px; background: linear-gradient(90deg, var(--band-start), var(--sun)); }
  .contact {
    position: absolute;
    left: 165px; top: 165px;
  }
  .contact__name {
    font-family: "Exo 2", sans-serif;
    font-weight: 600;
    font-size: 20px;
    color: var(--plum);
    margin-bottom: 7px;
  }
  .contact__line {
    font-family: "PT Sans Narrow", sans-serif;
    font-size: 16.5px;
    line-height: 21px;
    color: var(--ink);
  }
</style>
</head>
<body>
  <section class="card card--front">
    <div class="brand">LEDGER OWL</div>
  </section>

  <section class="card card--back">
    <p class="call-to-action">Looking for a more relaxed, friendly and<br>interactive relationship with your accountant?</p>
    <div class="band band--plum"></div>
    <div class="contact">
      <h1 class="contact__name">Gus Tarrow</h1>
      <p class="contact__line">Email:&nbsp; gus@ledgerowl.com.au</p>
      <p class="contact__line">Website:&nbsp; www.ledgerowl.com.au</p>
      <p class="contact__line">Phone:&nbsp; 1300 762 349</p>
    </div>
    <div class="band band--sun"></div>
  </section>
</body>
</html>
```